Packaging for Pim&Nora High quality baby teether and accessories

We need a packaging box with a front window for our baby teether line of product. The product line consists of different teether for baby. Safety, quality and design are our key features. We have proposed a color palette available in the photos but we would like to see some creative design with abstract forms. We are open to suggestions for the colors as long as the focus stays on the product inside the box. Design must be gender neutral as it is for boys and girls. Our product packaging need to be bilingual French and English with French being bigger(for the product name) then english in the design. You can play with our logo and adapt the color to fit your design(AI files have been provided).
Available files:
• Die Cut Template
• Logo (Adobe Illustrator)
• Color palette example
• Inspiration example
• Product pictures
• Abstract artsy design and colors
• Gender neutral
• NO ANIMALS
• NO Bright colors
• Textures and colors
• Embossed logo (shiny)
• Front window (transparent plastic) to be added on die cut template: rounded corners (measurement from each side: (suggestions)(top)20mmx(right)20mmx(left)20mmx(bottom)30mm
• Might be used for other products so must be easily adaptable
Here is what we should find on each side of the packaging: the way you present it is yours.
Front :
• Product name: Hochet de dentition / Rattle Teether
• Age : à partir de 6 mois / from 6 months
• Brand logo
Side 1:
• Disclaimer
• Bar code
• Importé par / imported by: Travonne advices inc.
o Belvoir, QC, Canada, J0X 1A0
• Conçu au Canada/Fabriqué en Chine
• Designed in Canada/Made in China
• CE logo
Back:
• Product advantages: with icons. Clean and refined (NOT jammed)
o Apprentissage/learning
o Doux sur les gencive/soft on gum
o Développement moteur/helps develop motricity
o Peut aider à Appaiser l’anxiété/Can help reduce anxiety
• Avantage conception:
o BPA free
o Phtalates free
o Lead Free
Back OR side
• Entretient/maintenance care:
o Nos produits sont faits de matériaux neufs seulement et de bois non traité. Nous recommandons le lavage à la main et le séchage à l’air libre. Our products are made from new material only and from untreated wood. We recommend hand washing and air drying.
Side 2:
• Could have a little something but should stay clean.
Botton:
• Blank
Target Market(s)
high end mass market, young family and friends. trendy products
Industry/Entity Type
Baby
Look and feel

```html
<!DOCTYPE html>
<html lang="fr">
<head>
<meta charset="utf-8">
<title>Pim&amp;Nora – Hochet de dentition / Rattle Teether – die line</title>
<link rel="stylesheet" href="https://fonts.googleapis.com/css2?family=Big+Shoulders+Display:wght@300;400;600&family=Open+Sans:wght@400&display=swap">
<style>
  :root{
    --plum:#673f4d;
    --plum-soft:#6b4a57;
    --ink:#111111;
    --cut:#ff0000;
    --fold:#00e600;
    --paper:#ffffff;
    --tone-pink:#ecd6df;
    --tone-slate:#e2e4e8;
    --tone-navy:#dde3ea;
    --tone-ochre:#f3e3d2;
  }
  html,body{margin:0;padding:0;}
  body{width:1200px;height:1000px;overflow:hidden;background:var(--paper);position:relative;
       font-family:"Big Shoulders Display",sans-serif;color:var(--ink);}
  .dieline{position:absolute;left:0;top:0;width:1200px;height:1000px;}
  .panel-text{position:absolute;margin:0;}

  /* back panel */
  .back-heading{left:136px;font-weight:600;font-size:30px;letter-spacing:-0.8px;line-height:1;}
  .back-heading.advantages{top:272px;}
  .back-heading.care{top:586px;}
  .advantage{position:absolute;left:136px;display:flex;align-items:center;gap:8px;
             font-weight:300;font-size:18px;white-space:nowrap;}
  .advantage .icon{width:30px;height:30px;border-radius:50%;background:var(--ink);flex:none;}
  .free-list{left:136px;top:482px;font-weight:300;font-size:27px;line-height:31px;
             color:var(--plum-soft);letter-spacing:1.5px;}
  .care-copy{left:135px;top:618px;width:300px;font-weight:300;font-size:15.5px;line-height:23px;}

  /* front panel */
  .title-band{position:absolute;left:633px;top:257px;width:307px;height:43px;border-radius:8px;
              background:var(--plum);color:#fff;display:flex;align-items:center;justify-content:center;
              font-weight:400;font-size:27px;letter-spacing:-0.3px;white-space:nowrap;}
  .title-band .sep{margin:0 8px;}
  .age-ribbon{position:absolute;left:652px;top:342px;width:120px;transform:rotate(-45deg);
              transform-origin:center center;
              color:#fff;font-weight:400;font-size:13px;line-height:13px;text-align:center;}
  .brand-band{position:absolute;left:633px;top:655px;width:307px;height:62px;border-radius:8px;
              background:var(--plum);display:flex;align-items:center;justify-content:center;gap:14px;}
  .brand-band .dot{width:26px;height:26px;border-radius:50%;background:#fff;opacity:.85;}
  .brand-band .name{color:#fff;font-weight:300;font-size:46px;letter-spacing:1px;}

  /* side 1 */
  .vertical{position:absolute;transform-origin:left top;transform:rotate(-90deg);
            white-space:nowrap;font-weight:300;font-size:13px;line-height:13px;}
  .origin-fr{left:964px;top:571px;}
  .origin-en{left:983px;top:566px;}
  .address{left:1093px;top:555px;}
  .disclaimer-tab{position:absolute;left:1009px;top:455px;width:26px;height:102px;
                  border:2px solid var(--ink);box-sizing:border-box;background:#fff;}
  .disclaimer-tab span{position:absolute;left:3px;top:96px;transform-origin:left top;transform:rotate(-90deg);
                       font-family:"Open Sans",sans-serif;font-size:12px;letter-spacing:.5px;white-space:nowrap;}
  .disclaimer-box{position:absolute;left:1036px;top:385px;width:48px;height:243px;
                  border:2px solid var(--ink);box-sizing:border-box;}
  .cert-mark{position:absolute;left:1072px;top:288px;width:28px;height:21px;border-radius:4px;background:var(--ink);}
  .importer{left:987px;top:670px;width:100px;text-align:center;font-weight:300;font-size:15px;line-height:20px;}
</style>
</head>
<body>

<svg class="dieline" viewBox="0 0 1200 1000" role="img"
     aria-label="Die-cut box layout; all panels carry a terrazzo pattern of muted pink, slate, navy and ochre chips on white">
  <defs>
    <linearGradient id="terrazzo" x1="0" y1="0" x2="1" y2="1">
      <stop offset="0" stop-color="var(--tone-pink)"/>
      <stop offset=".3" stop-color="#faf6f8"/>
      <stop offset=".55" stop-color="var(--tone-slate)"/>
      <stop offset=".8" stop-color="var(--tone-ochre)"/>
      <stop offset="1" stop-color="var(--tone-navy)"/>
    </linearGradient>
  </defs>

  <g fill="url(#terrazzo)" stroke="var(--cut)" stroke-width="2.2" stroke-linejoin="round">
    <polygon points="79,258 119,249 119,749 79,739"/>
    <rect x="119" y="249" width="334" height="500"/>
    <polygon points="125,249 125,94 127,94 127,66 444,66 444,94 447,94 447,249"/>
    <rect x="453" y="249" width="168" height="500"/>
    <polygon points="457,249 457,227 466,220 485,144 619,144 619,249"/>
    <polygon points="457,749 457,771 466,778 485,854 619,854 619,749"/>
    <rect x="621" y="249" width="332" height="500"/>
    <rect x="621" y="86" width="332" height="163"/>
    <path d="M621,86 L621,70 Q621,40 651,40 L923,40 Q953,40 953,70 L953,86 Z"/>
    <rect x="621" y="749" width="332" height="163"/>
    <path d="M621,912 L621,928 Q621,960 651,960 L923,960 Q953,960 953,928 L953,912 Z"/>
    <rect x="953" y="249" width="164" height="500"/>
    <polygon points="953,249 953,144 1089,144 1109,220 1117,229 1117,249"/>
    <polygon points="953,749 953,854 1089,854 1109,778 1117,769 1117,749"/>
  </g>

  <g fill="#fff" stroke="var(--cut)" stroke-width="2.2">
    <path d="M250,121 L322,121 A9.5,9.5 0 0 1 322,140 L300,140 A14,14 0 0 1 272,140 L250,140 A9.5,9.5 0 0 1 250,121 Z"/>
    <path d="M250,205 L272,205 A14,14 0 0 1 300,205 L322,205 A9.5,9.5 0 0 1 322,224 L250,224 A9.5,9.5 0 0 1 250,205 Z"/>
  </g>

  <rect x="666" y="307" width="243" height="319" rx="23" fill="#fff" stroke="var(--cut)" stroke-width="2.5"/>
  <polygon points="743,308 774,308 666,426 666,383" fill="var(--plum)"/>

  <g stroke="var(--fold)" stroke-width="2.2">
    <line x1="119" y1="249" x2="1117" y2="249"/>
    <line x1="119" y1="749" x2="1117" y2="749"/>
    <line x1="125" y1="171" x2="444" y2="171"/>
    <line x1="119" y1="249" x2="119" y2="749"/>
    <line x1="453" y1="249" x2="453" y2="749"/>
    <line x1="621" y1="249" x2="621" y2="749"/>
    <line x1="953" y1="249" x2="953" y2="749"/>
    <line x1="1117" y1="249" x2="1117" y2="749"/>
    <line x1="648" y1="86" x2="926" y2="86"/>
    <line x1="648" y1="912" x2="926" y2="912"/>
  </g>
</svg>

<!-- back panel -->
<h2 class="panel-text back-heading advantages">PRODUCT ADVANTAGES:</h2>
<div class="advantage" style="top:309px"><span class="icon"></span>PEUT AIDER À APPAISER L’ANXIÉTÉ/CAN HELP REDUCE ANXIETY</div>
<div class="advantage" style="top:350px"><span class="icon"></span>DÉVELOPPEMENT MOTEUR/HELPS DEVELOP MOTRICITY</div>
<div class="advantage" style="top:392px"><span class="icon"></span>DOUX SUR LES GENCIVE/SOFT ON GUM</div>
<div class="advantage" style="top:433px"><span class="icon"></span>APPRENTISSAGE/LEARNING</div>
<p class="panel-text free-list">BPA FREE<br>LEAD FREE<br>PHTALATES FREE</p>
<h2 class="panel-text back-heading care">ENTRETIENT/MAINTENANCE CARE:</h2>
<p class="panel-text care-copy">NOS PRODUITS SONT FAITS DE MATÉRIAUX NEUFS SEULEMENT ET DE BOIS NON TRAITÉ. NOUS RECOMMANDONS LE LAVAGE À LA MAIN ET LE SÉCHAGE À L’AIR LIBRE.<br>OUR PRODUCTS ARE MADE FROM NEW MATERIAL ONLY AND FROM UNTREATED WOOD. WE RECOMMEND HAND WASHING AND AIR DRYING.</p>

<!-- front panel -->
<div class="title-band">HOCHET DE DENTITION<span class="sep">|</span>RATTLE TEETHER</div>
<div class="age-ribbon">FROM 6 MONTHS/<br>À PARTIR DE 6 MOIS</div>
<div class="brand-band"><span class="dot"></span><span class="name">Pim&amp;Nora</span></div>

<!-- side 1 -->
<span class="cert-mark" role="img" aria-label="Conformity certification mark"></span>
<p class="panel-text vertical origin-fr">CONÇU AU CANADA/FABRIQUÉ EN CHINE</p>
<p class="panel-text vertical origin-en">DESIGNED IN CANADA/MADE IN CHINA</p>
<div class="disclaimer-box"></div>
<div class="disclaimer-tab"><span>DISCLAIMER</span></div>
<p class="panel-text vertical address">BELVOIR, QC, CANADA, J0X 1A0</p>
<p class="panel-text importer">IMPORTÉ PAR/<br>IMPORTED BY:<br>TRAVONNE ADVICES INC.</p>

</body>
</html>
```